Professional Photography Business cards

I need business cards that include my logo which I have uploaded. I run a photography business. I am open to ideas but I would like one side to have my logo and the other side to have my contact info. I don't have a website made but I do own a website domain. I have uploaded 2 different logo color schemes. My business colors are Blue, black , and white.

Business Name
Business Phone Number
Business Email
Business Website address
Instagram

Industry/Entity Type

Professional Photography

Contact Information for Business Card

Phone Number: 555-304-7826 email: info@tkale-studio.example Instagram: @t.kalestudio website doman- www.tkale-studio.example

Requirements
Must have
• I like the idea of a business card with a full black background front and back of card. My colors must include royal blue, black, and white

```html
<!DOCTYPE html>
<html lang="en">
<head>
<meta charset="utf-8">
<title>T. Kale Studio — Business Card</title>
<link rel="stylesheet" href="https://fonts.googleapis.com/css2?family=Montserrat:wght@700&family=Roboto:wght@400;500&display=swap">
<style>
  :root {
    --royal: #3d4ad6;
    --royal-soft: #6470e6;
    --card-black: #0b0b0d;
    --card-black-lift: #1b1c24;
    --paper: #ffffff;
    --muted: #c9cbd6;
    --backdrop: #d7d8de;
  }
  * { box-sizing: border-box; margin: 0; padding: 0; }
  html, body {
    width: 1200px; height: 929px; overflow: hidden;
    background: var(--backdrop);
    font-family: "Roboto", Arial, sans-serif;
  }
  .canvas { position: relative; width: 1200px; height: 929px; }

  .card {
    position: absolute;
    width: 620px; height: 354px;
    border-radius: 18px;
    background: radial-gradient(circle at 68% 70%, var(--card-black-lift), var(--card-black) 70%);
    box-shadow: 0 14px 30px rgba(0,0,0,.35);
    overflow: hidden;
  }

  .brand { display: flex; align-items: center; gap: 14px; color: var(--paper); }
  .brand__dot {
    width: 30px; height: 30px; border-radius: 50%;
    border: 3px solid var(--royal);
  }
  .brand__name {
    font-family: "Roboto", Arial, sans-serif;
    font-weight: 500;
    letter-spacing: 1px;
  }

  /* Front: brand side */
  .card--front {
    left: 90px; top: 70px;
    display: flex; align-items: center; justify-content: center;
    border-top: 6px solid var(--royal);
  }
  .card--front .brand__name { font-size: 44px; }

  /* Back: contact side */
  .card--back { left: 490px; top: 500px; border-bottom: 6px solid var(--royal); }
  .card--back .brand { position: absolute; left: 38px; top: 112px; }
  .card--back .brand__name { font-size: 26px; }
  .card--back .brand__dot { width: 22px; height: 22px; border-width: 2px; }

  .divider {
    position: absolute; left: 290px; top: 44px;
    width: 2px; height: 180px; background: var(--royal);
  }
  .contact { position: absolute; left: 312px; top: 40px; }
  .contact__name {
    font-family: "Montserrat", Arial, sans-serif;
    font-weight: 700; font-size: 21px; color: var(--royal-soft);
    letter-spacing: .3px;
  }
  .contact__role { font-size: 16px; color: var(--muted); margin: 2px 0 12px 0; }
  .contact__list { list-style: none; }
  .contact__item {
    display: flex; align-items: center; gap: 9px;
    font-size: 16px; color: var(--paper); line-height: 27px;
    white-space: nowrap;
  }
  .contact__item svg { width: 15px; height: 15px; fill: var(--royal-soft); flex: none; }

  .address {
    position: absolute; left: 38px; bottom: 40px;
    display: flex; align-items: center; gap: 8px;
    font-size: 18px; color: var(--muted);
  }
  .address svg { width: 16px; height: 20px; fill: var(--royal-soft); }
</style>
</head>
<body>
<main class="canvas">
  <section class="card card--front" aria-label="Card front">
    <div class="brand">
      <span class="brand__dot"></span>
      <span class="brand__name">T. Kale Studio</span>
    </div>
  </section>

  <section class="card card--back" aria-label="Card back">
    <div class="brand">
      <span class="brand__dot"></span>
      <span class="brand__name">T. Kale Studio</span>
    </div>

    <div class="divider"></div>

    <div class="contact">
      <h1 class="contact__name">TOMAS KALE</h1>
      <p class="contact__role">Professional Photographer</p>
      <ul class="contact__list">
        <li class="contact__item">
          <svg viewBox="0 0 16 16"><path d="M3 1h3l1.5 4-2 1.3a9 9 0 0 0 4.2 4.2L11 8.5l4 1.5v3a2 2 0 0 1-2 2A13 13 0 0 1 1 3a2 2 0 0 1 2-2z"/></svg>
          555-304-7826
        </li>
        <li class="contact__item">
          <svg viewBox="0 0 16 16"><path d="M1 3h14v10H1z M1 3l7 6 7-6" fill="none" stroke="#6470e6" stroke-width="1.6"/></svg>
          info@tkale-studio.example
        </li>
        <li class="contact__item">
          <svg viewBox="0 0 16 16"><circle cx="8" cy="8" r="6"/></svg>
          @t.kalestudio
        </li>
        <li class="contact__item">
          <svg viewBox="0 0 16 16"><circle cx="8" cy="8" r="7"/><path d="M1 8h14M8 1c-3 3.5-3 10.5 0 14M8 1c3 3.5 3 10.5 0 14" stroke="#0b0b0d" stroke-width="1" fill="none"/></svg>
          www.tkale-studio.example
        </li>
      </ul>
    </div>

    <p class="address">
      <svg viewBox="0 0 16 20"><path d="M8 0a7 7 0 0 1 7 7c0 5-7 13-7 13S1 12 1 7a7 7 0 0 1 7-7zm0 4a3 3 0 1 0 0 6 3 3 0 0 0 0-6z"/></svg>
      4120 Harbor Mill Lane Springdale, Oh 45000
    </p>
  </section>
</main>
</body>
</html>
```